Business cards, stationery and report cover
For market research and marketing company in New Zealand
Simple
Rosalind Thorpe
Level 1
57 Pemberly Road
Milford
Auckland
PO Box 46-582
Auckland 0963
rosalind@lumenvex.co.nz
www.lumenvex.co.nz
From this process we are looking for business cards, letterhead, comp slip, as well as a generic cover page and inside page for our reports (e.g heading styles, footers etc). Both report pages need to be easily replicated or applied to Microsoft Word reports. We are PC users if this makes a difference.
The information for the business cards can be on the front or the back - depending on your design and what looks best. Most people would contact us by phone/cell/email.
We would like to be viewed as professional, competent, modern and well established. We don't want to look like we are an advertising agency, or quirky or too different from our competitors. However, we'd like to be eye catching and interesting! Our typical clients are intelligent managers who are over 35 years and a mixture of male and female.
Please let us know if you have any questions or would like clarification on anything.
As noted in 'Additional Comments' you can choose what details would look best on the front of the business card, and which you would recommend going on the back of the card.
This is our new logo.

```html
<!DOCTYPE html>
<html lang="en">
<head>
<meta charset="utf-8">
<title>Lumenvex stationery set</title>
<link href="https://fonts.googleapis.com/css2?family=Open+Sans:wght@400;600;700&display=swap" rel="stylesheet">
<style>
  :root {
    --stage: #3f3a37;
    --paper: #ffffff;
    --paper-shade: #f1f1f1;
    --brand-blue: #2b80c3;
    --brand-grey: #5b5c5e;
    --brand-dark: #444547;
    --ink: #4d4d4f;
    --ink-soft: #9a9a9c;
  }
  * { box-sizing: border-box; margin: 0; padding: 0; }
  html, body { width: 1200px; height: 422px; overflow: hidden; }
  body {
    background: var(--stage);
    font-family: "Open Sans", Arial, sans-serif;
    color: var(--ink);
    position: relative;
  }
  .piece { position: absolute; background: var(--paper); box-shadow: 0 2px 6px rgba(0,0,0,.35); overflow: hidden; }
  .brand-name { font-family: "Open Sans", Arial, sans-serif; font-weight: 600; color: var(--brand-blue); letter-spacing: .2px; line-height: 1; white-space: nowrap; }
  .brand-name.on-dark { color: var(--paper); }
  .brand-dot { display: inline-block; width: .45em; height: .45em; border-radius: 50%; background: currentColor; margin-right: .3em; vertical-align: .1em; }

  /* business cards */
  .card { width: 116px; height: 66px; }
  .card--logo { left: 34px; top: 41px; display: flex; align-items: center; justify-content: center; }
  .card--contact { left: 158px; top: 41px; padding: 8px 9px; }
  .card--grey { left: 34px; top: 115px; background: var(--brand-grey); display: flex; align-items: center; justify-content: center; }
  .card--blue { left: 158px; top: 115px; background: var(--brand-blue); display: flex; align-items: center; justify-content: center; }
  .card .brand-name { font-size: 15px; }
  .card--contact .brand-name { font-size: 9px; }
  .contact-name { font-size: 5.5px; font-weight: 700; margin-top: 8px; text-align: right; }
  .contact-lines { font-size: 4px; line-height: 1.35; margin-top: 3px; text-align: right; color: var(--ink-soft); }

  /* envelopes */
  .envelope { width: 246px; height: 66px; left: 34px; }
  .envelope svg { position: absolute; inset: 0; }
  .envelope--back { top: 200px; }
  .envelope--front { top: 240px; left: 40px; }
  .envelope--plain { top: 283px; left: 46px; background: var(--paper-shade); }

  /* compliments slips */
  .comp-slip { width: 188px; height: 82px; top: 307px; padding: 10px 12px; }
  .comp-slip--a { left: 233px; }
  .comp-slip--b { left: 439px; }
  .comp-slip .brand-name { font-size: 10px; }
  .comp-text { position: absolute; left: 12px; bottom: 10px; font-size: 5px; color: var(--ink-soft); }

  /* letterheads */
  .letterhead { top: 41px; width: 178px; height: 246px; }
  .letterhead--a { left: 304px; }
  .letterhead--b { left: 510px; width: 200px; height: 262px; }
  .letterhead .brand-name { position: absolute; left: 50%; top: 16px; transform: translateX(-50%); font-size: 11px; }
  .letterhead svg { position: absolute; left: 0; bottom: 0; width: 100%; }
  .letter-footer { position: absolute; left: 0; right: 0; bottom: 8px; text-align: center; font-size: 3.6px; color: var(--ink-soft); }

  /* report cover */
  .report-cover { left: 732px; top: 41px; width: 192px; height: 266px; background: var(--paper); }
  .report-cover .brand-name { position: absolute; left: 30px; top: 68px; font-size: 20px; }
  .cover-band { position: absolute; left: 0; top: 108px; width: 100%; }
  .cover-title { position: absolute; left: 0; right: 0; top: 152px; text-align: center; color: var(--paper); }
  .cover-title h1 { font-size: 13px; font-weight: 700; letter-spacing: .3px; }
  .cover-title p { font-size: 6.5px; }
  .cover-photo { position: absolute; left: 0; top: 176px; width: 100%; height: 50px; background: linear-gradient(100deg, #6e5a52 0%, #a88274 45%, #c14a3c 75%, #6b3b33 100%); }
  .cover-base { position: absolute; left: 0; bottom: 0; width: 100%; height: 40px; background: var(--brand-grey); }

  /* inside page */
  .inside-page { left: 941px; top: 41px; width: 230px; height: 271px; }
  .inside-header { height: 16px; background: var(--brand-grey); color: var(--paper); font-size: 5px; text-align: right; padding: 5px 8px 0; }
</style>
</head>
<body>

  <!-- Business cards -->
  <div class="piece card card--logo"><span class="brand-name">lumenvex</span></div>
  <div class="piece card card--contact">
    <span class="brand-name">lumenvex</span>
    <p class="contact-name">Rosalind Thorpe</p>
    <p class="contact-lines">57 Pemberly Road<br>PO Box 46-582, Auckland 0963<br>rosalind@lumenvex.co.nz<br>www.lumenvex.co.nz</p>
  </div>
  <div class="piece card card--grey"><span class="brand-name on-dark">lumenvex</span></div>
  <div class="piece card card--blue"><span class="brand-name on-dark">lumenvex</span></div>

  <!-- Envelopes -->
  <div class="piece envelope envelope--back">
    <svg viewBox="0 0 246 66" preserveAspectRatio="none"><path d="M0 0 L123 36 L246 0 Z" fill="var(--brand-blue)"/></svg>
  </div>
  <div class="piece envelope envelope--front">
    <svg viewBox="0 0 246 66" preserveAspectRatio="none"><path d="M0 0 L123 38 L246 0 Z" fill="var(--brand-grey)"/></svg>
  </div>
  <div class="piece envelope envelope--plain"></div>

  <!-- Compliments slips -->
  <div class="piece comp-slip comp-slip--a">
    <span class="brand-name">lumenvex</span>
  </div>
  <div class="piece comp-slip comp-slip--b">
    <span class="brand-name">lumenvex</span>
    <p class="comp-text">With Compliments</p>
  </div>

  <!-- Letterheads -->
  <div class="piece letterhead letterhead--a">
    <span class="brand-name">lumenvex</span>
    <svg viewBox="0 0 178 40" preserveAspectRatio="none" height="40">
      <path d="M0 14 Q90 40 178 6 L178 40 L0 40 Z" fill="var(--brand-blue)"/>
      <path d="M0 22 Q90 44 178 16 L178 40 L0 40 Z" fill="var(--paper)"/>
    </svg>
    <p class="letter-footer">57 Pemberly Road · PO Box 46-582 · Auckland 0963 · www.lumenvex.co.nz</p>
  </div>
  <div class="piece letterhead letterhead--b">
    <span class="brand-name">lumenvex</span>
    <p class="letter-footer">57 Pemberly Road · PO Box 46-582 · Auckland 0963 · www.lumenvex.co.nz</p>
  </div>

  <!-- Report cover -->
  <div class="piece report-cover">
    <span class="brand-name"><span class="brand-dot"></span>lumenvex</span>
    <svg class="cover-band" viewBox="0 0 192 70" preserveAspectRatio="none" height="70">
      <path d="M0 30 Q96 8 192 24 L192 70 L0 70 Z" fill="var(--brand-grey)"/>
      <path d="M0 34 Q96 14 192 30" fill="none" stroke="var(--brand-blue)" stroke-width="3"/>
    </svg>
    <div class="cover-title">
      <h1>FRONT COVER</h1>
      <p>Your text can move here</p>
    </div>
    <div class="cover-photo" role="img" aria-label="Report cover photograph"></div>
    <div class="cover-base"></div>
  </div>

  <!-- Inside report page -->
  <div class="piece inside-page">
    <div class="inside-header">Your text can move here</div>
  </div>

</body>
</html>
```